Redesign of business card for Birchline Mechanical

We are looking for a new design for our business cards for Birchline Mechanical. We are a plumbing & HVAC construction company, operating on the West Coast of Canada and USA. Logo attached.
Industry/Entity Type
Construction - Plumbing & HVAC
Contact Information for Business Card
Name, address, phone numbers, email, website address
Look and feel
Each slider illustrates characteristics of the customer's brand and the style your logo design should communicate.

```html
<!DOCTYPE html>
<html lang="en">
<head>
<meta charset="utf-8">
<title>Birchline Mechanical – Business Card</title>
<link href="https://fonts.googleapis.com/css2?family=Poppins:wght@400;500;700&display=swap" rel="stylesheet">
<style>
  :root {
    --page: #ffffff;
    --ink: #0b0b0c;
    --front-bg: #151617;
    --front-edge: #050506;
    --back-bg: #e8e6e8;
    --white: #ffffff;
    --rule: #5a3a3c;
    --art-tone: #d9d9db;
  }
  * { margin: 0; padding: 0; box-sizing: border-box; }
  html, body { width: 1200px; height: 1000px; overflow: hidden; background: var(--page); }
  body { position: relative; font-family: "Poppins", sans-serif; color: var(--ink); }

  .card {
    position: absolute;
    left: 195px;
    width: 810px;
    height: 464px;
    border-radius: 18px;
    overflow: hidden;
  }

  /* Front */
  .card-front {
    top: 30px;
    background: radial-gradient(ellipse at 50% 40%, var(--front-bg) 0%, var(--front-edge) 100%);
  }
  .front-brand {
    position: absolute;
    left: 0; right: 0;
    top: 192px;
    text-align: center;
    font-weight: 500;
    font-size: 34px;
    letter-spacing: 1px;
    color: var(--white);
  }
  .front-brand .brand-square {
    display: inline-block;
    width: 22px; height: 22px;
    border: 4px solid var(--white);
    margin-right: 12px;
    vertical-align: -1px;
  }
  .plumbing-art {
    position: absolute;
    left: 0;
    top: 118px;
    width: 810px;
    height: 300px;
  }

  /* Back */
  .card-back {
    top: 506px;
    background: var(--back-bg);
  }
  .contact-block {
    position: absolute;
    left: 60px;
    top: 24px;
    width: 310px;
    text-align: center;
  }
  .person-name { font-weight: 700; font-size: 30px; line-height: 1.3; }
  .person-title { font-weight: 500; font-size: 18px; margin-top: 2px; }
  .icon-row {
    display: flex;
    align-items: center;
    justify-content: center;
    gap: 6px;
    margin-top: 18px;
  }
  .icon-rule { width: 70px; height: 1px; background: var(--rule); margin: 0 6px; }
  .icon-box {
    width: 26px; height: 26px;
    background: var(--ink);
    display: flex; align-items: center; justify-content: center;
  }
  .contact-lines { margin-top: 17px; font-weight: 500; font-size: 18.5px; }
  .contact-lines p { line-height: 35.5px; }

  .back-brand {
    position: absolute;
    right: 36px;
    top: 44px;
    font-weight: 500;
    font-size: 19px;
    color: var(--ink);
  }
  .back-brand .brand-square {
    display: inline-block;
    width: 14px; height: 14px;
    border: 3px solid var(--ink);
    margin-right: 8px;
    vertical-align: -1px;
  }

  .skyline-art {
    position: absolute;
    left: 0; right: 0;
    top: 286px;
    bottom: 0;
    background: linear-gradient(180deg, #1a1a1b 0%, var(--ink) 40%);
  }
  .address {
    position: absolute;
    left: 0; right: 0;
    bottom: 14px;
    text-align: center;
    color: var(--white);
    font-size: 19.5px;
    font-weight: 400;
  }
  .address svg { vertical-align: -2px; margin-right: 6px; }
</style>
</head>
<body>

  <section class="card card-front">
    <div class="front-brand"><span class="brand-square"></span>Birchline Mechanical</div>

    <svg class="plumbing-art" role="img" aria-label="White plumbing pipe line with couplings, a tap and a hand holding a wrench" viewBox="0 0 810 300" preserveAspectRatio="none">
      <path fill="var(--art-tone)" fill-opacity="0.16" d="M0 210 H670 V0 H810 V300 H0 Z"/>
    </svg>
  </section>

  <section class="card card-back">
    <div class="contact-block">
      <h1 class="person-name">Marcus Hale</h1>
      <p class="person-title">Managing Director</p>
      <div class="icon-row">
        <span class="icon-rule"></span>
        <span class="icon-box">
          <svg width="16" height="14" viewBox="0 0 16 14" fill="var(--white)"><path d="M1 5 Q8 0 15 5 L13 7 L11 5 H5 L3 7 Z"/><rect x="3" y="7" width="10" height="6" rx="1"/></svg>
        </span>
        <span class="icon-box">
          <svg width="18" height="13" viewBox="0 0 18 13" fill="none" stroke="var(--white)" stroke-width="1.5"><rect x="1" y="1" width="16" height="11"/><path d="M1 1 L9 7 L17 1"/></svg>
        </span>
        <span class="icon-box">
          <svg width="16" height="16" viewBox="0 0 16 16" fill="none" stroke="var(--white)" stroke-width="1.4"><circle cx="8" cy="8" r="6.5"/><ellipse cx="8" cy="8" rx="3" ry="6.5"/><line x1="1.5" y1="8" x2="14.5" y2="8"/></svg>
        </span>
        <span class="icon-rule"></span>
      </div>
      <div class="contact-lines">
        <p>044-555 018 372</p>
        <p>info@birchlinemech.com</p>
        <p>www.birchlinemech.com</p>
      </div>
    </div>

    <div class="back-brand"><span class="brand-square"></span>Birchline Mechanical</div>

    <div class="skyline-art" role="img" aria-label="City skyline silhouette with a construction crane"></div>

    <p class="address">
      <svg width="12" height="16" viewBox="0 0 12 16" fill="var(--white)"><path d="M6 0 C2.7 0 0 2.6 0 5.8 C0 10 6 16 6 16 C6 16 12 10 12 5.8 C12 2.6 9.3 0 6 0 Z M6 8 A2.2 2.2 0 1 1 6 3.6 A2.2 2.2 0 1 1 6 8 Z"/></svg>Unit 210, 48 Harbourview Road, Port Alder, WA 98012-4471
    </p>
  </section>

</body>
</html>
```